Quiet Harbor Business Card
QH biz card design 1
Quiet Harbor Business Card - Funerals
Creative Brief
Simple
Marcus Pelley
2417 Linden Crossway, Ste 42 Maple Falls, MN 55990
marcus@quietharbr.com
www.quietharbr.com

```html
<!DOCTYPE html>
<html lang="en">
<head>
<meta charset="utf-8">
<title>Quiet Harbor Business Card</title>
<link rel="stylesheet" href="https://fonts.googleapis.com/css2?family=Cinzel:wght@400&family=Cormorant+Garamond:wght@500&display=swap">
<style>
  :root {
    --page: #e9e9e9;
    --card: #ffffff;
    --ink-dark: #3e3e3e;
    --ink-mid: #555555;
    --accent-soft: #c9b7c9;
    --accent-fade: #e4dae4;
  }
  html, body {
    margin: 0;
    width: 1200px;
    height: 777px;
    overflow: hidden;
    background: var(--page);
  }
  .stage {
    position: relative;
    width: 1200px;
    height: 777px;
  }
  .card {
    position: absolute;
    width: 560px;
    height: 320px;
    background: var(--card);
    box-shadow: 0 1px 3px rgba(0,0,0,0.12);
    overflow: hidden;
  }
  .card--front { left: 40px; top: 40px; }
  .card--back { left: 600px; top: 417px; }

  .brand {
    position: absolute;
    left: 0; right: 0;
    display: flex;
    align-items: center;
    justify-content: center;
    gap: 16px;
  }
  .card--front .brand { top: 38px; }
  .brand__square {
    display: block;
    border: 5px solid var(--ink-dark);
    box-sizing: border-box;
  }
  .card--front .brand__square { width: 58px; height: 58px; }
  .brand__name {
    font-family: "Cinzel", serif;
    font-weight: 400;
    color: var(--ink-dark);
    letter-spacing: 0.12em;
    text-transform: uppercase;
    white-space: nowrap;
  }
  .card--front .brand__name { font-size: 34px; }

  .holder {
    position: absolute;
    top: 140px; left: 0; right: 0;
    margin: 0;
    text-align: center;
    font-family: "Cinzel", serif;
    font-weight: 400;
    font-size: 24px;
    color: var(--ink-mid);
    letter-spacing: 0.04em;
  }
  .contact {
    position: absolute;
    top: 196px; left: 0; right: 0;
    text-align: center;
    font-family: "Cormorant Garamond", serif;
    font-weight: 500;
    font-size: 16px;
    line-height: 21px;
    color: var(--ink-mid);
  }
  .contact p { margin: 0; }
  .contact__address { font-variant: small-caps; letter-spacing: 0.02em; }
  .contact__web { display: inline-block; margin-left: 24px; }

  .accent-bar {
    position: absolute;
    left: 0; right: 0;
    bottom: 36px;
    height: 8px;
    background: linear-gradient(90deg, var(--accent-fade), var(--accent-soft));
  }

  .card--back .brand {
    top: 0; bottom: 0;
    flex-direction: column;
    gap: 22px;
  }
  .card--back .brand__square { width: 150px; height: 150px; border-width: 14px; }
  .card--back .brand__name { font-size: 30px; }
</style>
</head>
<body>
<main class="stage">
  <section class="card card--front" aria-label="Business card front">
    <div class="brand">
      <span class="brand__square"></span>
      <span class="brand__name">Quiet Harbor</span>
    </div>
    <h1 class="holder">Marcus Pelley</h1>
    <div class="contact">
      <p class="contact__address">2417 Linden Crossway, Ste 42 Maple Falls, MN 55990</p>
      <p>651-555-0142 &nbsp;/&nbsp; 651-555-0187</p>
      <p>marcus@quietharbr.com<span class="contact__web">www.quietharbr.com</span></p>
    </div>
    <div class="accent-bar" role="img" aria-label="Decorative colour band along the lower edge"></div>
  </section>

  <section class="card card--back" aria-label="Business card back">
    <div class="brand">
      <span class="brand__square"></span>
      <span class="brand__name">Quiet Harbor</span>
    </div>
  </section>
</main>
</body>
</html>
```